Redesign Colorful Business Card

Please redesign the card attached. It is too busy. Please don't eliminate any of the words. The repetivite word "free" can be used less often.

Target Market(s)

College Students.

Contact Information for Business Card

The details listed in the attached image

Font styles to use
Sans Serif

Requirements
Must have
• A clear and simple presentation and must be attractive.

```html
<!DOCTYPE html>
<html lang="en">
<head>
<meta charset="utf-8">
<title>StudyBrisk Business Card</title>
<link rel="stylesheet" href="https://fonts.googleapis.com/css2?family=Archivo+Black&family=Mulish:wght@300;400&family=Archivo:wght@800&display=swap">
<style>
  :root {
    --page: #ffffff;
    --card-dark: #121a21;
    --card-mid: #1f2731;
    --card-light: #343c47;
    --ribbon: #d2232a;
    --accent: #00aeef;
    --ink-dark: #16202a;
    --body-text: #b7bcc3;
    --white: #ffffff;
    --mascot-cool: #5cb8cf;
    --mascot-warm: #b5529c;
    --mascot-gold: #c99a3c;
  }
  * { margin: 0; padding: 0; box-sizing: border-box; }
  html, body {
    width: 1200px; height: 1200px; overflow: hidden;
    background: var(--page);
  }
  .canvas { position: relative; width: 1200px; height: 1200px; }

  .card {
    position: absolute; left: 145px; top: 342px;
    width: 917px; height: 524px;
    border-radius: 44px; overflow: hidden;
    background: linear-gradient(210deg, var(--card-light) 0%, var(--card-mid) 45%, var(--card-dark) 100%);
  }

  .ribbon { position: absolute; left: 0; top: 0; width: 300px; height: 220px; }
  .ribbon-text {
    position: absolute; left: 35px; top: 55px;
    width: 200px;
    transform: rotate(-38deg);
    font-family: "Archivo", sans-serif; font-weight: 800;
    font-size: 23px; line-height: 25px;
    color: var(--white); text-align: center; letter-spacing: 0.2px;
  }

  .emblem { position: absolute; left: 51px; top: 74px; width: 420px; height: 420px; }
  .emblem-glow {
    position: absolute; left: 22px; top: 22px; width: 376px; height: 376px;
    border-radius: 50%;
    background: conic-gradient(from 0deg, #ef3b3c, #f7693a 40deg, #f8e236 90deg, #9bd142 130deg, #1fb47a 155deg, #3a5bc8 190deg, #3c2f7a 240deg, #5a2a52 290deg, #b02c3c 330deg, #ef3b3c);
    filter: blur(10px);
  }
  .emblem-ring {
    position: absolute; left: 22px; top: 22px; width: 376px; height: 376px;
    border-radius: 50%;
    background: linear-gradient(160deg, #222b35, #171e26);
  }
  .emblem-disc {
    position: absolute; left: 49px; top: 49px; width: 322px; height: 322px;
    border-radius: 50%;
    background: radial-gradient(circle at 45% 40%, #1a222b, #111519 90%);
    box-shadow: inset 6px 8px 18px rgba(0,0,0,0.55);
  }
  .mascot-art {
    position: absolute; left: 104px; top: 78px; width: 222px; height: 222px;
    border-radius: 50%;
    background: linear-gradient(110deg, var(--mascot-cool) 0%, var(--mascot-warm) 55%, var(--mascot-gold) 100%);
    opacity: 0.8;
  }

  .free-tag {
    position: absolute; left: 467px; top: 65px;
    width: 148px; height: 57px;
    background: var(--accent);
    font-family: "Archivo Black", sans-serif;
    font-size: 44px; line-height: 57px; letter-spacing: 1px;
    color: var(--ink-dark); text-align: center;
  }
  .feature-rail {
    position: absolute; left: 531px; top: 122px;
    width: 2px; height: 242px; background: var(--accent);
  }
  .features { position: absolute; left: 525px; top: 0; list-style: none; }
  .feature {
    position: absolute; left: 0; width: 320px;
    font-family: "Mulish", sans-serif; font-weight: 300;
    font-size: 27px; line-height: 28px; color: var(--body-text);
    padding-left: 33px; white-space: nowrap;
  }
  .feature::before {
    content: ""; position: absolute; left: 0; top: 8px;
    width: 14px; height: 14px; background: var(--accent);
  }
  .feature-1 { top: 156px; }
  .feature-2 { top: 234px; }
  .feature-3 { top: 312px; }

  .website-line {
    position: absolute; left: 467px; top: 424px;
    width: 385px;
    display: flex; align-items: flex-end;
  }
  .website {
    font-family: "Mulish", sans-serif; font-weight: 400;
    font-size: 40px; line-height: 48px; color: var(--accent);
    white-space: nowrap;
  }
  .website-rule {
    flex: 1; height: 2px; margin: 0 0 11px 6px;
    background: var(--accent);
  }
</style>
</head>
<body>
<div class="canvas">
  <section class="card">
    <svg class="ribbon" viewBox="0 0 300 220" aria-hidden="true">
      <polygon points="141,0 237,0 0,186 0,109" fill="var(--ribbon)"/>
    </svg>
    <div class="ribbon-text">ENROLL NOW<br>FOR FREE</div>

    <div class="emblem">
      <div class="emblem-glow"></div>
      <div class="emblem-ring"></div>
      <div class="emblem-disc"></div>
      <div class="mascot-art" role="img" aria-label="Colourful elephant mascot illustration"></div>
    </div>

    <div class="free-tag">FREE</div>
    <div class="feature-rail"></div>
    <ul class="features">
      <li class="feature feature-1">Learn a subject without<br>having to go to class.</li>
      <li class="feature feature-2">Cut study time down by<br>up to 50%.</li>
      <li class="feature feature-3">Memorize anything<br>quickly.</li>
    </ul>

    <div class="website-line">
      <span class="website">StudyBrisk.com</span>
      <span class="website-rule"></span>
    </div>
  </section>
</div>
</body>
</html>
```